Structural Engineering Business Card

Veltrow Drafts does residential house plans for clients in Central Florida. Would like simple but elegant business card that is appropriate for a house plan engineering company. Prefer black business card with black/white them but open to other shades of blue. I uploaded a sample card that I came across that looked good but please come up with your own creative designs.

Contact Information for Business Card

Name, Title, Phone, Email, Address, website

```html
<!DOCTYPE html>
<html lang="en">
<head>
<meta charset="utf-8">
<title>Veltrow Drafts – Business Card</title>
<link rel="stylesheet" href="https://fonts.googleapis.com/css2?family=Lato:wght@400;700;900&display=swap">
<style>
  :root {
    --stage: #e9e9e7;
    --card-dark: #141414;
    --card-dark-2: #2a2a2a;
    --card-mid: #1d1d1d;
    --card-light: #ffffff;
    --ink: #111111;
    --paper: #ffffff;
    --muted: #d6d6d6;
  }
  * { box-sizing: border-box; margin: 0; padding: 0; }
  html, body { width: 1200px; height: 801px; overflow: hidden; }
  body {
    background: var(--stage);
    font-family: "Lato", sans-serif;
    position: relative;
  }
  .card {
    position: absolute;
    width: 540px;
    height: 310px;
    border-radius: 18px;
    overflow: hidden;
    box-shadow: 0 10px 28px rgba(0,0,0,0.22);
  }
  .card--front { left: 50px; top: 245px; background: var(--card-dark); }
  .card--back  { left: 610px; top: 245px; background: var(--card-mid); }

  .backdrop {
    position: absolute; inset: 0;
    background: radial-gradient(ellipse at 70% 45%, #333333 0%, var(--card-dark-2) 35%, var(--card-dark) 80%);
  }
  .card--front .wordmark {
    position: absolute;
    left: 0; right: 0; top: 128px;
    text-align: center;
    font-weight: 900;
    font-size: 46px;
    letter-spacing: 1px;
    color: var(--paper);
    text-transform: uppercase;
  }

  .back-shape { position: absolute; inset: 0; width: 100%; height: 100%; }
  .card--back .wordmark {
    position: absolute;
    left: 40px; top: 184px;
    font-weight: 900;
    font-size: 26px;
    color: var(--ink);
    text-transform: uppercase;
  }
  .contact {
    position: absolute;
    left: 330px; top: 62px;
    color: var(--paper);
  }
  .contact__name { font-weight: 700; font-size: 22px; letter-spacing: .5px; }
  .contact__title { font-size: 14px; color: var(--muted); margin: 2px 0 14px; }
  .contact__list { list-style: none; font-size: 12.5px; }
  .contact__list li { display: flex; align-items: flex-start; gap: 8px; margin-bottom: 6px; }
  .contact__list li.phone { font-weight: 700; font-size: 14px; }
  .contact__list svg { width: 12px; height: 12px; flex: none; margin-top: 2px; fill: var(--paper); }
</style>
</head>
<body>

<section class="card card--front" aria-label="Card front">
  <div class="backdrop" role="img" aria-label="Faint architectural house blueprint drawing on a dark background"></div>
  <div class="wordmark">Veltrow Drafts</div>
</section>

<section class="card card--back" aria-label="Card back">
  <div class="backdrop" role="img" aria-label="Faint architectural floor plan drawing on a dark background"></div>
  <svg class="back-shape" viewBox="0 0 540 310" preserveAspectRatio="none" role="img" aria-label="Large white state map silhouette">
    <path d="M0 70 C200 80 280 95 300 150 C330 230 420 250 470 310 H0 Z" fill="#ffffff"/>
  </svg>
  <div class="wordmark">Veltrow Drafts</div>
  <div class="contact">
    <div class="contact__name">DANIEL KORR</div>
    <div class="contact__title">Founder &amp; CEO</div>
    <ul class="contact__list">
      <li class="phone">
        <svg viewBox="0 0 24 24"><path d="M6.6 10.8a15 15 0 0 0 6.6 6.6l2.2-2.2c.3-.3.7-.4 1-.2 1.1.4 2.3.6 3.6.6.6 0 1 .4 1 1V20c0 .6-.4 1-1 1A17 17 0 0 1 3 4c0-.6.4-1 1-1h3.5c.6 0 1 .4 1 1 0 1.3.2 2.5.6 3.6.1.3 0 .7-.2 1z"/></svg>
        (555) 204-3178
      </li>
      <li>
        <svg viewBox="0 0 24 24"><path d="M2 5h20v14H2z M2 5l10 8 10-8" fill="none" stroke="#fff" stroke-width="2"/></svg>
        office@veltrowdrafts.com
      </li>
      <li>
        <svg viewBox="0 0 24 24"><circle cx="12" cy="12" r="9" fill="none" stroke="#fff" stroke-width="2"/><path d="M3 12h18M12 3c3 3 3 15 0 18M12 3c-3 3-3 15 0 18" fill="none" stroke="#fff" stroke-width="1.5"/></svg>
        www.veltrowdrafts.com
      </li>
      <li>
        <svg viewBox="0 0 24 24"><path d="M12 2a7 7 0 0 0-7 7c0 5 7 13 7 13s7-8 7-13a7 7 0 0 0-7-7zm0 9.5A2.5 2.5 0 1 1 12 6.5a2.5 2.5 0 0 1 0 5z"/></svg>
        <span>Your Address, City<br>State, Zip 1235</span>
      </li>
    </ul>
  </div>
</section>

</body>
</html>
```